2 Independent chilean winemakers here!
La Ventisca (means door slam or slam), that is the brand for our wines (2 wines at the moment), low scale production.
We would like to have front label for our wine out of the mainstream typical french classic style. Some words to describe it: youthful yet vintage/ Osric Penwell/ brantley/ comic/ old western. Something i would wear on a t-shirt.
The text that is has to be on the label:
- La Ventisca (the brand)
-Field Blend (the type of one of the wines we have)
- 2018
- Wine of Chile.
It goes on sloping shoulder bottle, Burgundy model.
It is meant to cover a space of 3 1/4 h x 4 1/2 w inches . (or 8,5 cm height x 11cm width).
We like colours so...be creative!
I have attached the "La Ventisca" logo. We can changed it of course.
Thanks !

young drinkers (legally allowed to drink!)

• stencil

• Obvious wine things like glasses of wine, vines, grapes etc.

```html
<!DOCTYPE html>
<html lang="en">
<head>
<meta charset="utf-8">
<title>La Ventisca – Field Blend 2018 front label</title>
<link rel="stylesheet" href="https://fonts.googleapis.com/css2?family=Roboto+Condensed:wght@400;700&family=Archivo+Black&display=swap">
<style>
  :root {
    --backdrop: #bdbcb8;
    --paper: #efebe2;
    --paper-light: #f4f1ea;
    --red: #e3172b;
    --blue: #1fa3cf;
    --ink: #1c1a1a;
    --band: #3a3636;
    --white: #ffffff;
  }
  html, body {
    margin: 0;
    width: 1200px;
    height: 1000px;
    overflow: hidden;
    background: var(--backdrop);
  }
  .wine-label {
    position: absolute;
    left: 100px;
    top: 114px;
    width: 1000px;
    height: 772px;
    display: block;
  }
  .paper { fill: var(--paper); }
  .paper-strip { fill: var(--paper-light); }
  .accent-red { fill: var(--red); }
  .accent-blue { fill: var(--blue); }
  .band-dark { fill: var(--band); }
  .ink { fill: var(--ink); }
  .stripe-white { fill: var(--white); }
  .brand-name {
    font-family: "Roboto Condensed", sans-serif;
    font-weight: 700;
    font-size: 62px;
    fill: var(--ink);
  }
  .wine-type {
    font-family: "Roboto Condensed", sans-serif;
    font-size: 26px;
    fill: var(--red);
  }
  .maker-line {
    font-family: "Roboto Condensed", sans-serif;
    font-size: 26px;
    fill: var(--ink);
  }
  .vintage {
    font-family: "Archivo Black", sans-serif;
    font-size: 34px;
    fill: var(--ink);
  }
  .origin {
    font-family: "Roboto Condensed", sans-serif;
    font-weight: 700;
    font-size: 23px;
    fill: var(--white);
  }
  .volume {
    font-family: "Roboto Condensed", sans-serif;
    font-size: 23px;
    fill: var(--ink);
  }
</style>
</head>
<body>
<svg class="wine-label" viewBox="0 0 1000 772" xmlns="http://www.w3.org/2000/svg">
  <defs>
    <clipPath id="label-edge">
      <path d="M0 0 H1000 V760 L990 772 L980 760 L970 772 L960 760 L950 772 L940 760 L930 772 L920 760 L910 772 L900 760 L890 772 L880 760 L870 772 L860 760 L850 772 L840 760 L830 772 L820 760 L810 772 L800 760 L790 772 L780 760 L770 772 L760 760 L750 772 L740 760 L730 772 L720 760 L710 772 L700 760 L690 772 L680 760 L670 772 L660 760 L650 772 L640 760 L630 772 L620 760 L610 772 L600 760 L590 772 L580 760 L570 772 L560 760 L550 772 L540 760 L530 772 L520 760 L510 772 L500 760 L490 772 L480 760 L470 772 L460 760 L450 772 L440 760 L430 772 L420 760 L410 772 L400 760 L390 772 L380 760 L370 772 L360 760 L350 772 L340 760 L330 772 L320 760 L310 772 L300 760 L290 772 L280 760 L270 772 L260 760 L250 772 L240 760 L230 772 L220 760 L210 772 L200 760 L190 772 L180 760 L170 772 L160 760 L150 772 L140 760 L130 772 L120 760 L110 772 L100 760 L90 772 L80 760 L70 772 L60 760 L50 772 L40 760 L30 772 L20 760 L10 772 L0 760 Z"/>
    </clipPath>
    <radialGradient id="letter-scatter" cx="0.5" cy="0.5" r="0.5">
      <stop offset="0" stop-color="#1fa3cf" stop-opacity="0.55"/>
      <stop offset="0.6" stop-color="#1fa3cf" stop-opacity="0.25"/>
      <stop offset="1" stop-color="#1fa3cf" stop-opacity="0"/>
    </radialGradient>
  </defs>

  <g clip-path="url(#label-edge)">
    <rect class="paper" width="1000" height="772"/>
    <rect class="paper-strip" width="147" height="772"/>
    <rect class="paper-strip" x="872" width="128" height="772"/>

    <!-- corner triangles -->
    <polygon class="accent-blue" points="654,0 1000,0 1000,500"/>
    <polygon class="accent-red" points="0,515 0,772 257,772"/>

    <!-- scattered lettering texture -->
    <rect x="120" y="0" width="780" height="772" fill="url(#letter-scatter)"
          role="img" aria-label="Scattered repeated letters in blue, red and black spreading across the label"/>

    <!-- horizontal band -->
    <rect class="band-dark" x="0" y="473" width="600" height="29"/>

    <!-- brand name -->
    <rect class="accent-red" x="301" y="392" width="48" height="48"/>
    <text class="brand-name" x="364" y="440" textLength="360" lengthAdjust="spacingAndGlyphs">LA VENTISCA</text>

    <text class="wine-type" x="455" y="497">Field Blend</text>
    <text class="maker-line" x="608" y="497" textLength="238" lengthAdjust="spacingAndGlyphs">INDEPENDANT WINEMAKERS</text>

    <text class="vintage" x="301" y="560">2018</text>

    <!-- bottom info bar -->
    <polygon class="ink" points="301,672 640,672 684,716 301,716"/>
    <text class="origin" x="330" y="703">WINE OF CHILE</text>
    <polygon class="stripe-white" points="560,672 578,672 622,716 604,716"/>
    <polygon class="stripe-white" points="590,672 608,672 652,716 634,716"/>
    <polygon class="stripe-white" points="620,672 638,672 682,716 664,716"/>
    <text class="volume" x="696" y="707">75 cl</text>
    <text class="volume" x="762" y="707">Alk.14% vol</text>

    <polygon class="ink" points="878,672 898,672 942,716 922,716"/>
    <polygon class="ink" points="910,672 930,672 974,716 954,716"/>
    <polygon class="ink" points="942,672 962,672 1000,710 1000,716 986,716"/>
    <polygon class="ink" points="974,672 994,672 1000,678 1000,698"/>
  </g>
</svg>
</body>
</html>
```